New shirt company looking for a fun and edgy online retail website design

We're a new company looking for a simple yet attractive website to sell shirts/tops to a mostly younger female audience. Our name is Tavi Shirt Co. and the PlanHerd logo is uploaded. We're thinking a home page, three separate pages for our shirt "collections", and a contact page/cart page for a grand total of 5 pages. We'd like the website to be coded, easy for the consumer to navigate/shop/checkout, and easy to link to various social media platforms and online websites. For colors, we're aiming for various blues, light grey, and maybe tan/khaki. Our goal is to launch with approximately 20-30 tops/shirts (or 7-10) per page. Please let us know if you have any questions and thank you for helping us! We are very excited to see what is created!

Target Market(s)

Female teens to early twenties

Coding

Coded - Design and coding required

Number of Pages Required

3 page

Font styles to use
Decorative
Script

Colors
cee9f5
85cae6
33a6d7
0393ce
cfdfed
85acd3

Requirements
Must have
• Online shopping/purchasing capabilities, dropdowns to select sizes for each item, easy to add/remove new or seasoned items.

```html
<!DOCTYPE html>
<html lang="en">
<head>
<meta charset="utf-8">
<title>Tavi Shirt Co. — Product</title>
<link rel="stylesheet" href="https://fonts.googleapis.com/css2?family=Montserrat:wght@400;500;600;700&display=swap">
<style>
  :root{
    --sky-pale:#cee9f5;
    --sky:#85cae6;
    --blue:#33a6d7;
    --blue-deep:#0393ce;
    --ink:#2b2b2b;
    --grey-box:#e8e8e8;
    --footer:#222222;
    --footer-bottom:#1b1b1b;
    --footer-tile:#303030;
    --white:#ffffff;
  }
  *{box-sizing:border-box;margin:0;padding:0}
  html,body{width:1200px;height:3355px;overflow:hidden}
  body{position:relative;background:var(--white);font-family:'Montserrat',sans-serif;color:var(--ink)}
  .abs{position:absolute}

  /* header */
  .brand-box{left:64px;top:0;width:206px;height:106px;background:var(--sky);display:flex;align-items:center;justify-content:center}
  .brand-name{font-weight:600;font-size:20px;color:#1d4f8c}
  .nav{top:46px;left:517px;display:flex;gap:0;font-size:16px;font-weight:500;text-transform:uppercase}
  .nav a{position:absolute;white-space:nowrap;text-decoration:none;color:var(--ink)}
  .nav a.active{color:var(--blue)}
  .icon-btn{width:42px;height:42px;border-radius:50%;background:var(--blue-deep);top:35px;display:flex;align-items:center;justify-content:center}

  /* hero */
  .hero-frame{left:327px;top:178px;width:545px;height:542px;border:1px solid var(--blue)}
  .hero-photo{position:absolute;inset:0;background:linear-gradient(180deg,#e8d6b8 0%,#cdc3b8 35%,#bdb4aa 70%,#5f7088 100%)}
  .arrow{top:388px}
  .dot{width:12px;height:12px;border-radius:50%;top:750px;background:#8a8a8a}
  .dot.on{background:var(--blue-deep)}
  .product-title{top:782px;left:0;width:1200px;text-align:center;font-size:28px;font-weight:600}
  .price{font-size:26px;color:var(--blue)}
  .price s{font-weight:600}
  .price b{font-weight:700}
  .price span{font-weight:400}
  .hero-price{left:271px;top:870px}
  .size-select{left:520px;top:862px;width:185px;height:50px;background:var(--grey-box);border:1px solid #bdbdbd;display:flex;align-items:center;justify-content:center;gap:12px;font-size:18px;font-weight:500}
  .add-cart{left:748px;top:860px;width:180px;height:55px;background:var(--blue-deep);color:var(--white);display:flex;align-items:center;justify-content:center;gap:8px;font-size:14px;font-weight:600}
  .delivery{top:954px;left:0;width:1200px;text-align:center;font-size:15px;font-weight:500}

  /* detail band */
  .band{left:0;top:1031px;width:1200px;height:1739px;background:var(--sky-pale)}
  .section-title{left:0;width:1200px;text-align:center;font-size:33px;font-weight:600;color:var(--blue)}
  .copy{left:180px;width:840px;text-align:center;font-size:17.5px;line-height:36px;font-weight:400}
  .thumb{width:258px;height:258px;border-radius:50%;top:1694px;background:radial-gradient(circle at 50% 40%,#e4d5bd 0%,#d4cbc2 45%,#f2f2f2 80%)}
  .card{top:2136px;width:279px;height:451px;background:var(--white)}
  .card-photo{position:absolute;left:0;top:0;width:279px;height:249px}
  .card-title{position:absolute;top:264px;left:0;width:279px;text-align:center;font-size:21px;line-height:27px;font-weight:600}
  .card-price{position:absolute;top:330px;left:0;width:279px;text-align:center;font-size:22px}
  .btn{background:var(--blue-deep);color:var(--white);font-size:14px;font-weight:600;display:flex;align-items:center;justify-content:center;text-transform:uppercase}
  .card .btn{position:absolute;left:75px;top:375px;width:129px;height:53px}
  .see-all{left:494px;top:2646px;width:212px;height:55px}
  .to-top{left:568px;top:2739px;width:62px;height:62px;border-radius:50%;background:var(--blue-deep);display:flex;align-items:center;justify-content:center;z-index:2}

  /* footer */
  .footer{left:0;top:2770px;width:1200px;height:465px;background:var(--footer)}
  .footer-bottom{left:0;top:3235px;width:1200px;height:120px;background:var(--footer-bottom)}
  .foot-brand{left:233px;top:2881px;width:145px;height:82px;background:var(--sky);display:flex;align-items:center;justify-content:center}
  .foot-brand .brand-name{font-size:15px}
  .contact-line{display:flex;align-items:center;gap:16px;color:var(--white);font-size:26px;font-weight:600}
  .ring{width:54px;height:54px;border:2px solid var(--white);border-radius:50%;display:flex;align-items:center;justify-content:center}
  .col-title{font-size:25px;color:var(--white);font-weight:500;top:2870px}
  .tile{width:202px;height:43px;background:var(--footer-tile);color:var(--white);font-size:16px;font-weight:500;display:flex;align-items:center;padding-left:24px;text-transform:uppercase}
  .copyright{left:64px;top:3279px;color:var(--white);font-size:16px}
  .pay{top:3269px;width:64px;height:41px;border-radius:3px;background:#f4f4f4}
</style>
</head>
<body>

<!-- header -->
<div class="abs brand-box"><span class="brand-name">Tavi Shirt Co.</span></div>
<nav class="abs nav">
  <a class="active" style="left:0">Home</a>
  <a style="left:91px">About us</a>
  <a style="left:216px">Collections</a>
  <a style="left:370px">Contact us</a>
</nav>
<div class="abs icon-btn" style="left:1029px" aria-label="Cart">
  <svg width="20" height="20" viewBox="0 0 24 24" fill="#fff"><path d="M2 3h3l2.6 11h11l2.4-8H7" stroke="#fff" stroke-width="2" fill="none"/><circle cx="9" cy="19" r="2"/><circle cx="17" cy="19" r="2"/></svg>
</div>
<div class="abs icon-btn" style="left:1094px" aria-label="Account">
  <svg width="20" height="20" viewBox="0 0 24 24" fill="#fff"><circle cx="12" cy="8" r="4.5"/><path d="M3 21c0-5 4-8 9-8s9 3 9 8z"/></svg>
</div>

<!-- hero -->
<div class="abs hero-frame"><div class="hero-photo" role="img" aria-label="Model wearing beige off-shoulder knit top with jeans"></div></div>
<svg class="abs arrow" style="left:172px" width="28" height="44" viewBox="0 0 28 44"><path d="M22 4L6 22l16 18" stroke="var(--blue-deep)" stroke-width="5" fill="none"/></svg>
<svg class="abs arrow" style="left:1000px" width="28" height="44" viewBox="0 0 28 44"><path d="M6 4l16 18L6 40" stroke="var(--blue-deep)" stroke-width="5" fill="none"/></svg>
<div class="abs dot on" style="left:569px"></div>
<div class="abs dot" style="left:593px"></div>
<div class="abs dot" style="left:618px"></div>

<h1 class="abs product-title">Tavi’s net sleeves&nbsp; black top beige colored 100% cotton #344453</h1>
<div class="abs price hero-price"><s>$30</s> <b>$25</b>&nbsp; <span>30%off</span></div>
<div class="abs size-select">select size <svg width="14" height="16" viewBox="0 0 14 16"><path d="M1 2l6 12 6-12" stroke="#2b2b2b" stroke-width="2" fill="none"/></svg></div>
<div class="abs add-cart">
  <svg width="20" height="18" viewBox="0 0 24 22" fill="#fff"><path d="M1 2h4l3 11h12l3-9H7z"/><circle cx="10" cy="18" r="2"/><circle cx="18" cy="18" r="2"/></svg>
  ADD TO CART
</div>
<p class="abs delivery">USUALLY DELIVERD IN 4-5 DAYS OF ORDERING.</p>

<!-- details -->
<div class="abs band"></div>
<h2 class="abs section-title" style="top:1072px">PRODUCT DESCRIPTION</h2>
<p class="abs copy" style="top:1133px">Lorem ipsum dolor sit amet, consectetur adipiscing elit, sed do eiusmod tempor incididunt ut labore et dolore magna aliqua. Lacus sed viverra tellus in hac. Netus et malesuada fames ac turpis egestas maecenas pharetra. Eu tincidunt tortor aliquam nulla. Felis donec et odio pellentesque diam volutpat commodo sed. Tincidunt augue interdum velit euismod in pellentesque massa placerat. In hac habitasse platea dictumst vestibulum rhoncus est. Semper viverra nam libero justo laoreet sit amet. Neque laoreet suspendisse interdum consectetur libero. Lorem ipsum dolor sit amet consectetur adipiscing elit pellentesque.</p>
<p class="abs copy" style="top:1421px">Neque ornare aenean euismod elementum nisi quis. Aliquam sem et tortor consequat id porta nibh. Turpis egestas integer eget aliquet nibh. Ut tortor pretium viverra suspendisse potenti nullam ac. Vestibulum sed arcu non odio. Amet nisl suscipit adipiscing bibendum est ultricies integer quis auctor. Mattis vulputate enim nulla aliquet porttitor lacus luctus accumsan.</p>

<h2 class="abs section-title" style="top:1601px">PRODUCT IMAGES</h2>
<div class="abs thumb" style="left:156px" role="img" aria-label="Beige off-shoulder top, front view"></div>
<div class="abs thumb" style="left:470px" role="img" aria-label="Beige cold-shoulder top variant"></div>
<div class="abs thumb" style="left:784px" role="img" aria-label="Beige off-shoulder top, alternate view"></div>

<h2 class="abs section-title" style="top:2052px">SIMILAR PRODUCTS</h2>

<div class="abs card" style="left:65px">
  <div class="card-photo" role="img" aria-label="Black lace-sleeve blouse" style="background:linear-gradient(180deg,#3a3a3a,#141414 70%,#f5f5f5 100%)"></div>
  <div class="card-title">Tavi’s net sleeves<br>black top #344453</div>
  <div class="card-price price"><s>$30</s> <b>$25</b>&nbsp; <span>30%off</span></div>
  <div class="btn">Know more</div>
</div>
<div class="abs card" style="left:461px">
  <div class="card-photo" role="img" aria-label="Beige off-shoulder knit top" style="background:linear-gradient(180deg,#e3d0b2,#c9c0b6 60%,#6e7c90 100%)"></div>
  <div class="card-title">Tavi’s net sleeves<br>black top #344453</div>
  <div class="card-price price"><s>$30</s> <b>$25</b>&nbsp; <span>30%off</span></div>
  <div class="btn">Know more</div>
</div>
<div class="abs card" style="left:856px">
  <div class="card-photo" role="img" aria-label="White wrap chiffon blouse" style="background:linear-gradient(180deg,#5a4335,#e9ecef 45%,#f4f4f4 100%)"></div>
  <div class="card-title">Tavi’s net sleeves<br>black top #344453</div>
  <div class="card-price price"><s>$30</s> <b>$25</b>&nbsp; <span>30%off</span></div>
  <div class="btn">Know more</div>
</div>

<div class="abs btn see-all">See all producTgs</div>

<!-- footer -->
<div class="abs footer"></div>
<div class="abs to-top"><svg width="26" height="16" viewBox="0 0 26 16"><path d="M3 13L13 3l10 10" stroke="#fff" stroke-width="4" fill="none"/></svg></div>

<div class="abs foot-brand"><span class="brand-name">Tavi Shirt Co.</span></div>
<div class="abs contact-line" style="left:170px;top:3008px">
  <div class="ring"><svg width="22" height="22" viewBox="0 0 24 24" fill="#fff"><path d="M6.6 10.8a15 15 0 0 0 6.6 6.6l2.2-2.2c.3-.3.7-.4 1-.2 1.1.4 2.3.6 3.6.6.6 0 1 .4 1 1V20c0 .6-.4 1-1 1A17 17 0 0 1 3 4c0-.6.4-1 1-1h3.5c.6 0 1 .4 1 1 0 1.3.2 2.5.6 3.6.1.3 0 .7-.2 1z"/></svg></div>
  5550 1234 1010
</div>
<div class="abs contact-line" style="left:112px;top:3100px">
  <div class="ring"><svg width="22" height="16" viewBox="0 0 22 16" fill="#fff"><rect x="0" y="0" width="22" height="16" rx="2"/><path d="M1 1l10 8 10-8" stroke="#222" stroke-width="2" fill="none"/></svg></div>
  contact@tavishirt.com
</div>

<div class="abs col-title" style="left:589px">EXPLORE</div>
<div class="abs tile" style="left:592px;top:2911px">Winter speciale</div>
<div class="abs tile" style="left:592px;top:2980px">Collection name</div>
<div class="abs tile" style="left:592px;top:3048px">The collections</div>
<div class="abs tile" style="left:592px;top:3117px">My cart</div>

<div class="abs col-title" style="left:885px">SITEMAP</div>
<div class="abs tile" style="left:886px;top:2911px">Home</div>
<div class="abs tile" style="left:886px;top:2980px">Collections</div>
<div class="abs tile" style="left:886px;top:3048px">Products</div>
<div class="abs tile" style="left:886px;top:3117px">Contact us</div>

<div class="abs footer-bottom"></div>
<p class="abs copyright">© Copyright Tavi Clothings&nbsp; pvt ltd</p>
<div class="abs pay" style="left:709px" aria-label="Payment method"></div>
<div class="abs pay" style="left:800px;background:#111;border:1px solid #555" aria-label="Payment method"></div>
<div class="abs pay" style="left:891px;background:#3e8fd6" aria-label="Payment method"></div>
<div class="abs pay" style="left:982px;background:#d63a3a" aria-label="Payment method"></div>
<div class="abs pay" style="left:1070px;background:#fff4c8" aria-label="Payment method"></div>

</body>
</html>
```